Brenwick Realty
Business cards and stationery
Brenwick Realty - Real Estate
Creative Brief
Modern
Marian Talcott
Director
Level 4 218 Garnet Lane Melbourne VIC 3000
marian@brenwickrealty-example.com.au
www.brenwickrealty-example.com.au
Brenwick Summit Realty 518902K Licensee Marian Talcott
Stationery needs to have the licensee info on the bottom of letterhead
black background logo in centre

```html
<!DOCTYPE html>
<html lang="en">
<head>
<meta charset="utf-8">
<title>Brenwick Realty – Business Card</title>
<link rel="stylesheet" href="https://fonts.googleapis.com/css2?family=Source+Sans+3:wght@400;600;700&display=swap">
<style>
  :root{
    --backdrop:#e9e6e1;
    --card:#0d0d0f;
    --magenta:#c8176f;
    --magenta-deep:#8e0f4e;
    --cyan:#2bb5e6;
    --white:#ffffff;
    --soft:#d9d9d9;
  }
  *{margin:0;padding:0;box-sizing:border-box}
  html,body{width:1200px;height:780px;overflow:hidden;background:var(--backdrop)}
  body{font-family:"Source Sans 3",Arial,sans-serif;position:relative}

  .business-card{
    position:absolute;left:100px;top:105px;width:1000px;height:570px;
    background:var(--card);border-radius:34px;overflow:hidden;
    box-shadow:0 10px 30px rgba(0,0,0,.25);
  }
  .accent-line{position:absolute;left:0;width:100%;height:3px;background:var(--cyan)}
  .accent-line--top{top:84px}
  .accent-line--bottom{top:196px}
  .brand-band{
    position:absolute;top:92px;height:100px;
    background:linear-gradient(180deg,var(--magenta) 0%,var(--magenta-deep) 100%);
  }
  .brand-band--left{left:0;width:280px}
  .brand-band--right{left:640px;width:360px}

  .brand-name{
    position:absolute;left:280px;width:360px;top:108px;
    display:flex;align-items:center;justify-content:center;gap:12px;
    color:var(--white);font-weight:700;font-size:38px;letter-spacing:.5px;
  }
  .brand-dot{width:18px;height:18px;border-radius:50%;background:var(--magenta);flex:none}

  .person{
    position:absolute;right:570px;top:272px;text-align:right;color:var(--white);
  }
  .person-name{color:var(--magenta);font-weight:600;font-size:31px;line-height:1.1}
  .person-title{color:var(--cyan);font-size:22px;line-height:1.3}
  .person-address{margin-top:34px;font-size:22px;line-height:1.4;font-style:normal}

  .divider{position:absolute;left:462px;top:280px;width:2px;height:240px;background:var(--soft);opacity:.8}

  .contact-list{position:absolute;left:488px;top:276px;list-style:none}
  .contact-item{display:flex;align-items:center;gap:14px;height:40px;color:var(--white);font-size:22px}
  .contact-icon{width:22px;height:22px;flex:none;fill:var(--magenta)}
</style>
</head>
<body>
  <article class="business-card">
    <div class="accent-line accent-line--top"></div>
    <div class="brand-band brand-band--left"></div>
    <div class="brand-band brand-band--right"></div>
    <div class="accent-line accent-line--bottom"></div>

    <div class="brand-name"><span class="brand-dot"></span>Brenwick Realty</div>

    <div class="person">
      <p class="person-name">Marian Talcott</p>
      <p class="person-title">Director</p>
      <address class="person-address">Level 4<br>218 Garnet Lane<br>Melbourne VIC 3000</address>
    </div>

    <div class="divider"></div>

    <ul class="contact-list">
      <li class="contact-item">
        <svg class="contact-icon" viewBox="0 0 24 24" aria-hidden="true"><path d="M6.6 10.8a15.1 15.1 0 0 0 6.6 6.6l2.2-2.2a1 1 0 0 1 1-.25 11.4 11.4 0 0 0 3.6.57 1 1 0 0 1 1 1V20a1 1 0 0 1-1 1A17 17 0 0 1 3 4a1 1 0 0 1 1-1h3.5a1 1 0 0 1 1 1c0 1.25.2 2.46.57 3.6a1 1 0 0 1-.25 1z"/></svg>
        03 9555 0142
      </li>
      <li class="contact-item">
        <svg class="contact-icon" viewBox="0 0 24 24" aria-hidden="true"><path d="M7 1h10a2 2 0 0 1 2 2v18a2 2 0 0 1-2 2H7a2 2 0 0 1-2-2V3a2 2 0 0 1 2-2zm0 3v14h10V4zm5 15.5a1.2 1.2 0 1 0 0 2.4 1.2 1.2 0 0 0 0-2.4z"/></svg>
        0400 555 217
      </li>
      <li class="contact-item">
        <svg class="contact-icon" viewBox="0 0 24 24" aria-hidden="true"><path d="M6 2h10l3 3v5h1a2 2 0 0 1 2 2v8a2 2 0 0 1-2 2H4a2 2 0 0 1-2-2v-8a2 2 0 0 1 2-2h2zm2 2v6h9V6h-2V4zm-2 10v2h4v-2zm7 0v2h2v-2zm3 0v2h2v-2z"/></svg>
        03 9555 0198
      </li>
      <li class="contact-item">
        <svg class="contact-icon" viewBox="0 0 24 24" aria-hidden="true"><path d="M2 5h20v14H2zm2 2v.5l8 5 8-5V7zm0 2.8V17h16V9.8l-8 5z"/></svg>
        marian@brenwickrealty-example.com.au
      </li>
      <li class="contact-item">
        <svg class="contact-icon" viewBox="0 0 24 24" aria-hidden="true"><path d="M12 2a10 10 0 1 0 0 20 10 10 0 0 0 0-20zm6.9 9h-3a15 15 0 0 0-1.3-5.4A8 8 0 0 1 18.9 11zM12 4.1c.9 1.2 1.8 3.6 2 6.9h-4c.2-3.3 1.1-5.7 2-6.9zM9.4 5.6A15 15 0 0 0 8.1 11h-3a8 8 0 0 1 4.3-5.4zM5.1 13h3a15 15 0 0 0 1.3 5.4A8 8 0 0 1 5.1 13zm6.9 6.9c-.9-1.2-1.8-3.6-2-6.9h4c-.2 3.3-1.1 5.7-2 6.9zm2.6-1.5a15 15 0 0 0 1.3-5.4h3a8 8 0 0 1-4.3 5.4z"/></svg>
        www.brenwickrealty-example.com.au
      </li>
    </ul>
  </article>
</body>
</html>
```